Redesign our business card for more impact

We want to completely replace the back design of our card, and refresh or even change the front entirely. We are happy with our black Q7 logo and do not want to change it.
Our company address changed too. It is now 58 Corvallen, Irvine, CA 92741
Updates

It was reported by Sketch Harbor email today that the uploaded files didnt upload. I am trying again.

Target Market(s)

Architects and Building Owners (People making multi-million dollar decisions)

Industry/Entity Type

Consulting Engineering

Contact Information for Business Card

Contact info on the front. "wallpaper" design on back with tag line on the back "Engineering Your Future"

Font styles to use
Sans Serif

Requirements
Must have
• A vivid, modern, impactful ...but tasteful back of card design. It should communicate our premier status, but grab attention as innovative. DESIGN SHOULD BE ELEGANT AND NOT TOO BUSY.
Nice to have
• Repeating pattern, multi-color, something creative...
Should not have
• Anything that looks too playful or that we are not serious professionals. It should also not be too boring or conservative.

```html
<!DOCTYPE html>
<html lang="en">
<head>
<meta charset="utf-8">
<title>Q7 Engineering – Business Card</title>
<link rel="stylesheet" href="https://fonts.googleapis.com/css2?family=Barlow:wght@300;400;600;700&display=swap">
<style>
  :root {
    --backdrop: #ababab;
    --card-grey: #68676b;
    --brand-orange: #fb8a40;
    --orange-deep: #ef7a30;
    --ink: #0d0d0f;
    --ink-soft: #2b2b2e;
  }
  * { margin: 0; padding: 0; box-sizing: border-box; }
  html, body {
    width: 1200px; height: 1000px; overflow: hidden;
    background: var(--backdrop);
    font-family: "Barlow", "Helvetica Neue", Arial, sans-serif;
  }
  .canvas { position: relative; width: 1200px; height: 1000px; }
  .card {
    position: absolute; top: 193px;
    width: 354px; height: 614px;
    overflow: hidden;
  }
  .card--front { left: 198px; background: var(--card-grey); }
  .card--back { left: 603px; background: var(--brand-orange); }

  .tagline {
    position: absolute; top: 29px; left: 0; right: 0;
    text-align: center; line-height: 1;
  }
  .tagline__main {
    display: block;
    font-weight: 700; font-size: 41px; letter-spacing: 4.5px;
    color: var(--ink);
  }
  .tagline__sub {
    display: block; margin-top: 5px;
    font-weight: 300; font-size: 35px; letter-spacing: 6.5px;
    color: var(--card-grey);
  }
  .card__brand {
    position: absolute; top: 190px; left: 0; right: 0; height: 190px;
    display: flex; align-items: center; justify-content: center;
    font-weight: 700; font-size: 200px; line-height: 1;
  }
  .card--front .card__brand { color: var(--ink); }
  .card--back .card__brand { color: var(--orange-deep); }

  .contact {
    position: absolute; left: 20px; right: 20px; top: 462px;
    text-align: center;
  }
  .contact__name {
    font-weight: 600; font-size: 31px; color: var(--ink);
    line-height: 1.1; margin-bottom: 6px;
  }
  .contact__line {
    font-weight: 300; font-size: 22.5px; color: var(--ink-soft);
    line-height: 32px;
  }
  .card__web {
    position: absolute; left: 0; right: 0; top: 564px;
    text-align: center; font-size: 22px; color: var(--ink-soft);
  }
  .card__web strong { font-weight: 700; }
</style>
</head>
<body>
<main class="canvas">
  <section class="card card--front" aria-label="Card front">
    <div class="card__brand">Q7</div>
    <div class="contact">
      <p class="contact__name">Daniel Reyes, Ceo</p>
      <p class="contact__line">daniel.reyes@q7eng.com</p>
      <p class="contact__line">(123) 456-7890 • q7eng.com</p>
      <p class="contact__line">58 Corvallen, Irvine, CA 92741</p>
    </div>
  </section>

  <section class="card card--back" aria-label="Card back">
    <h1 class="tagline">
      <span class="tagline__main">ENGINEERING</span>
      <span class="tagline__sub">YOUR FUTURE</span>
    </h1>
    <div class="card__brand">Q7</div>
    <p class="card__web"><strong>q7eng</strong>.com</p>
  </section>
</main>
</body>
</html>
```